Web Design Project

We are looking for a new site design for the VELTO Canada. The current site can be found at
http://www.veltocanada-example.org/
The URL is provided for reference. We want a completely different look and layout which is shown in the specifications document.
As part of the design, we want a home page, and inside page.
The design you provide will be implemented in Joomla. The design winner will only need to provide the PSD. We anticipate creating the template coding in-house.
However, if you have experience creating Joomla templates, please let us know as we may ask you to bid separately to do that phase of the project.
We've provided a specifications document which includes wireframes of the home page, and inside page. We've also included a logo file.
For the header at the top, as indicated in the specs document, we want to keep the same overall treatment to every page. We want a graphic treatment with the logo for the header area. In this manner, the design will be flexiable and can be used for future years.
For the home page, we've indicated that we'd like to have a slider implemented within the design.
The wireframe is provided to illustrate the placement of content and menu items. The exact dimensions of each component can be revised as you see fit. We are also flexiable if you feel we have missed items.

```html
<!DOCTYPE html>
<html lang="en">
<head>
<meta charset="utf-8">
<title>VELTO Canada</title>
<link href="https://fonts.googleapis.com/css2?family=Mulish:ital,wght@0,400;0,600;0,700;0,800;1,700&family=Ubuntu:ital,wght@0,400;0,500;1,700&display=swap" rel="stylesheet">
<style>
:root{
  --blue:#1b4a8f;
  --blue-dark:#163d78;
  --link:#2a4f95;
  --yellow:#ffd400;
  --red:#e0191b;
  --red-dark:#c10f12;
  --ink:#1f1f1f;
  --text:#3a3a3a;
  --muted:#7a7a7a;
  --panel:#ececec;
  --panel-2:#dedede;
  --page:#f4f4f4;
  --frame:#1c1c1c;
  --footer-dark:#1e1e1e;
}
*{margin:0;padding:0;box-sizing:border-box}
html,body{width:975px;height:1200px;overflow:hidden}
body{position:relative;background:var(--page);font-family:"Mulish",sans-serif;color:var(--text)}
.abs{position:absolute}

/* top bar */
.topbar{left:0;top:0;width:975px;height:25px;background:var(--blue);color:#fff;font-size:9px}
.topbar .contact{left:113px;top:7px;display:flex;gap:8px;align-items:center}
.topbar .contact svg{vertical-align:-1px;margin-right:4px}
.topbar .links{right:116px;top:7px;display:flex;gap:26px}
.topbar .links .active{color:var(--yellow)}

/* header */
.brand{left:124px;top:62px;display:flex;align-items:center;gap:8px}
.brand .dot{width:22px;height:22px;border-radius:50%;background:var(--red)}
.brand .name{font-weight:800;font-size:30px;color:var(--blue);letter-spacing:1px}
.social-top{left:597px;top:77px;display:flex;gap:4px}
.social-top span{width:19px;height:19px;border-radius:50%}

/* nav */
.mainnav{left:99px;top:158px;width:780px;height:46px;background:linear-gradient(#fafafa,#e9e9e9);display:flex;box-shadow:0 3px 4px rgba(0,0,0,.08)}
.mainnav .home{width:42px;height:46px;background:var(--blue);display:flex;align-items:center;justify-content:center}
.mainnav ul{list-style:none;display:flex;flex:1}
.mainnav li{font-size:11px;color:var(--ink);display:flex;align-items:center;justify-content:center;border-left:1px solid #dcdcdc;height:46px}
.mainnav li.current{color:var(--link)}

/* slider */
.slider{left:99px;top:233px;width:780px;height:322px;background:var(--frame);border-radius:5px;box-shadow:0 3px 6px rgba(0,0,0,.3)}
.slide{left:14px;top:16px;width:748px;height:289px;background:radial-gradient(ellipse at 50% 30%,#e08a3e 0%,#a2461a 45%,#5a2410 100%)}
.caption{left:221px;top:231px;width:287px;height:56px;background:linear-gradient(90deg,rgba(0,0,0,0),rgba(0,0,0,.55) 15%,rgba(0,0,0,.55) 85%,rgba(0,0,0,0));color:#fff;font-family:"Ubuntu",sans-serif;font-size:20px;line-height:25px;padding:1px 0 0 20px}
.caption .date{color:var(--yellow);font-weight:500}
.tab{top:148px;width:28px;height:24px;background:#fff;border:3px solid var(--red);border-radius:3px;display:flex;align-items:center;justify-content:center}
.tab i{width:10px;height:10px;border-radius:50%;background:#9a9a9a}

/* panels */
.panel{background:var(--panel)}
.panel h3{font-family:"Mulish",sans-serif;font-weight:600;font-size:12px;color:var(--ink);text-transform:uppercase;padding-bottom:6px;border-bottom:1px solid #b8b8b8}
.sponsors{left:99px;top:579px;width:147px;height:149px;padding:10px 10px}
.sponsor-name{margin:24px 0 0 14px;font-weight:800;font-size:30px;color:var(--blue)}
.btn-dark{background:var(--ink);color:#fff;font-size:11px;border-radius:14px;text-align:center}
.sponsors .btn-dark{position:absolute;left:8px;top:116px;width:128px;height:26px;line-height:26px}
.login{left:99px;top:741px;width:147px;height:150px;padding:10px 10px}
.field{width:128px;height:25px;margin-top:9px;border-radius:13px;background:#fff;border:1px solid #d2d2d2;font-size:9px;color:var(--muted);padding:7px 0 0 18px}
.field:first-of-type{margin-top:9px}
.remember{margin:7px 0 0 22px;font-size:9px;color:var(--muted);display:flex;align-items:center;gap:7px}
.remember i{width:10px;height:10px;border:1px solid #999;background:#fff}
.login .btn-dark{width:87px;height:20px;line-height:20px;margin:6px 0 0 20px;font-weight:700}

.feature{left:256px;top:579px;width:623px;height:312px}
.feature-photo{left:20px;top:17px;width:365px;height:115px;background:linear-gradient(180deg,#e9dfc9 0%,#c9a77a 55%,#5b4a3f 100%)}
.feature-lead{left:20px;top:142px;width:350px;font-weight:700;font-size:10px;line-height:17px;color:var(--ink)}
.feature-body{left:20px;top:183px;width:355px;font-size:9px;line-height:17px}
.read-more{left:20px;top:275px;width:70px;height:25px;background:var(--ink);color:#fff;font-size:8px;font-weight:800;line-height:25px;text-align:center}

.news{left:398px;top:17px;width:207px;height:278px;background:var(--panel-2);padding:9px 16px 0 17px}
.news h3{font-size:12px}
.news-item{padding:10px 0 0;font-size:8px;line-height:17px}
.news-item + .news-item{border-top:2px solid #b8b8b8;margin-top:6px}
.news-item .date{font-style:italic;color:var(--muted);font-size:7.5px}
.news-item .title{font-style:italic;font-weight:700;color:var(--ink);margin:2px 0 4px}
.news-item .title.hover{color:var(--link)}
.pager{right:11px;bottom:10px;display:flex;gap:3px}
.pager span{width:15px;height:15px;background:var(--ink);color:#fff;font-size:8px;font-weight:700;display:flex;align-items:center;justify-content:center}
.pager .on{background:var(--blue)}

.connected{left:99px;top:904px;width:147px;height:150px;padding:10px 10px}
.connected p{font-size:9px;line-height:17px;margin-top:8px}
.social-row{display:flex;gap:5px;margin:10px 0 0 3px}
.social-row span{width:24px;height:24px;border-radius:50%;background:#5a5a5a}
.social-row span.hl{background:#2aa4d8}

.regions{left:256px;top:904px;width:623px;height:150px;overflow:hidden}
.regions h3{position:absolute;left:19px;top:9px;width:139px;font-size:12px;text-transform:none}
.regions h3 span{text-transform:uppercase}
.map{right:0;top:0;width:203px;height:150px;background:radial-gradient(circle at 40% 35%,#e02b2b 0%,#e4e4e4 32%,#d9d9d9 100%)}
.cols{left:20px;top:46px;display:flex;font-size:9px;line-height:19px;color:var(--ink)}
.cols h4{font-weight:700;font-size:10px;margin-bottom:3px}
.cols div:nth-child(1){width:114px}
.cols div:nth-child(2){width:87px}
.cols div:nth-child(3){width:129px}
.cols div:nth-child(4){width:110px}
.cols .hover{color:var(--link);padding-left:9px}

/* twitter band */
.band{left:99px;top:1066px;width:780px;height:57px;background:linear-gradient(90deg,var(--red),var(--red-dark))}
.band .follow{left:126px;top:9px;font-family:"Ubuntu",sans-serif;font-style:italic;font-weight:700;font-size:14px;line-height:21px;color:#fff}
.band .quote{font-family:"Ubuntu",sans-serif;font-size:26px;color:rgba(255,255,255,.35);font-weight:700}

/* footer */
.footnav{left:0;top:1138px;width:975px;height:32px;background:var(--blue);display:flex;justify-content:center;align-items:center;gap:11px;font-size:9.5px;color:#fff}
.footnav .active{color:var(--yellow)}
.footnav .sep{font-size:8px}
.footbar{left:0;top:1170px;width:975px;height:30px;background:var(--footer-dark);display:flex;justify-content:center;align-items:center;gap:11px;font-size:9.5px;color:#fff}
</style>
</head>
<body>

<div class="abs topbar">
  <div class="abs contact">
    <span><svg width="9" height="9" viewBox="0 0 24 24" fill="#fff"><path d="M6.6 10.8a15 15 0 0 0 6.6 6.6l2.2-2.2c.3-.3.7-.4 1-.2 1.1.4 2.3.6 3.6.6.6 0 1 .4 1 1V20c0 .6-.4 1-1 1A17 17 0 0 1 3 4c0-.6.4-1 1-1h3.5c.6 0 1 .4 1 1 0 1.3.2 2.5.6 3.6.1.3 0 .7-.2 1z"/></svg>555-010-4827</span>
    <span>/</span>
    <span><svg width="10" height="8" viewBox="0 0 20 14" fill="#fff"><path d="M0 0h20v14H0zM1.5 1.5 10 8l8.5-6.5z" fill-rule="evenodd"/></svg>m.hartley@velto-example.ca</span>
  </div>
  <div class="abs links"><span class="active">Home</span><span>Contact Us</span><span>VELTO International</span></div>
</div>

<div class="abs brand"><span class="dot"></span><span class="name">VELTO</span></div>

<div class="abs social-top">
  <span style="background:#f57f20"></span><span style="background:#d9232d"></span><span style="background:#1a6ea8"></span><span style="background:#1d4f7c"></span><span style="background:#ea4c89"></span><span style="background:#e44134"></span><span style="background:#2f4a5f"></span><span style="background:#1ab7ea"></span><span style="background:#d92a22"></span><span style="background:#e8168d"></span><span style="background:#2aa4d8"></span><span style="background:#2f5597"></span>
</div>

<nav class="abs mainnav">
  <div class="home"><svg width="14" height="13" viewBox="0 0 24 22" fill="#fff"><path d="M12 1 1 11h3v10h6v-6h4v6h6V11h3z"/></svg></div>
  <ul>
    <li style="width:89px;border-left:0">About</li>
    <li style="width:81px">Board</li>
    <li class="current" style="width:92px">Chapters</li>
    <li style="width:118px">Member Space</li>
    <li style="width:163px">Resources &amp; Knowledge</li>
    <li style="width:110px">Sponsorship</li>
    <li style="width:85px">Exhibit</li>
  </ul>
</nav>

<div class="abs slider">
  <div class="abs slide" role="img" aria-label="Photo of a long wood-panelled boardroom table with leather chairs under warm lighting">
    <div class="abs caption">VELTO Canada Conference<br>Saskatoon.SK&nbsp; <span class="date">June 2-5.2013</span></div>
  </div>
</div>
<div class="abs tab" style="left:86px;top:381px"><i></i></div>
<div class="abs tab" style="left:861px;top:381px"><i></i></div>

<section class="abs panel sponsors">
  <h3>Sponsors</h3>
  <div class="sponsor-name">Northrel</div>
  <div class="btn-dark">Become a Sponsor</div>
</section>

<section class="abs panel login">
  <h3>Member Login</h3>
  <div class="field">Account login</div>
  <div class="field">Password</div>
  <div class="remember"><i></i>Remember Me</div>
  <div class="btn-dark">Login</div>
</section>

<section class="abs panel feature">
  <div class="abs feature-photo" role="img" aria-label="Photo of business people in a meeting around a table"></div>
  <p class="abs feature-lead">Etiam ullamcorper. Suspendisse a pellentesque dui, non feliss porta urna. Vestibulum commodo volutpat a, convallis ac, laoreet enim.</p>
  <p class="abs feature-body">Vestibulum commodo volutpat a, convallis ac, laoreet enim. erat ac ipsum. Integer aliquam purus. Quisque lorem tortor fringilla sed, vestibulum id, eleifend justo vel bibendum sapien massa ac turpis faucibus orci luctus non, consectetuer lobortis quis, varius in, purus. Vestibulum commodo volutpat a, convallis ac, laoreet enim. er lobortis quis, varius in, purus.</p>
  <div class="abs read-more">READ MORE</div>

  <div class="abs news">
    <h3>Latest News</h3>
    <div class="news-item">
      <div class="date">03.01.2013</div>
      <div class="title">Mobile Marketing: Too Big an Opportunity for Companies to Ignore</div>
      <div>Vestibulum commodo volutpat a, convallis ac, laoreet enim. erat ac ipsum. Integer aliquam purus.</div>
    </div>
    <div class="news-item">
      <div class="date">24.12.2012</div>
      <div class="title hover">Mobile Marketing: Too Big an Opportunity for Companies to Ignore</div>
      <div>Vestibulum commodo volutpat a, convallis ac, laoreet enim. erat ac ipsum. Integer aliquam purus.</div>
    </div>
    <div class="abs pager"><span class="on">1</span><span>2</span><span>&#9654;</span></div>
  </div>
</section>

<section class="abs panel connected">
  <h3>Stay Connected</h3>
  <p>Vestibulum commodo volut-pat a, convallis ac, laoreet.</p>
  <div class="social-row"><span></span><span class="hl"></span><span></span><span></span></div>
  <div class="social-row" style="margin-top:6px"><span></span><span></span><span></span></div>
</section>

<section class="abs panel regions">
  <div class="abs map" role="img" aria-label="Illustration of a magnifying glass over a world map highlighting Canada in red"></div>
  <h3><span>Regions</span></h3>
  <div class="abs cols">
    <div><h4>Mountain Pacific</h4>Vancouver Island<br>Vancouver<br>Calgary</div>
    <div><h4>Western</h4>Edmonton<br><span class="hover">Saskatchewan</span><br>Winnipeg</div>
    <div><h4>Central</h4>National Capital-Ottawa<br>Southwestern Ontario<br>Montreal<br>Toronto</div>
    <div><h4>Atlantic</h4>Nova Scotia<br>Terra Nova-St. John's<br>Prince Edward Island<br>Atlantic-St.John</div>
  </div>
</section>

<section class="abs band">
  <div class="abs follow">OF COURSE, DON'T FORGET TO FOLLOW US AT<br>@veltocanada-example.com</div>
  <div class="abs quote" style="left:434px;top:2px">&rdquo;</div>
  <div class="abs quote" style="left:754px;top:26px">&rdquo;</div>
</section>

<nav class="abs footnav">
  <span class="active">Home</span><span class="sep">&bull;</span><span>About</span><span class="sep">&bull;</span><span>Board</span><span class="sep">&bull;</span><span>Chapters</span><span class="sep">&bull;</span><span>Member Space</span><span class="sep">&bull;</span><span>Resources &amp; Knowledge</span><span class="sep">&bull;</span><span>Sponsorship</span><span class="sep">&bull;</span><span>Exhibit</span><span class="sep">&bull;</span><span>Member Login</span><span class="sep">&bull;</span><span>Contact Us</span>
</nav>
<footer class="abs footbar">
  <span>Privacy Policy</span><span>&bull;</span><span>Terms Of Use</span><span>&bull;</span><span>Privacy Statement &copy; Copyright 2013 by VELTO Canada International</span>
</footer>

</body>
</html>
```